Health Information/Education Logo Design

We need a logo design for a new company based in Atlanta called Brightpath Care. The program is about patient empowerment. We provide health information and education on how to get healthy, stay healthy, and how to be proactive in your care. We also provide medication and injection training to help patients feel their best and to ensure successful therapy outcomes.
We like the colors yellow, pink, teal and purple and would like to see some or all of these colors in the designs. The final design should communicate caring, considerate, compassionate information, education and training services
Education
Contact Information for Business Card
Brightpath Care
Lorraine Pettaway RN, MSN, MHA
Nurse Educator
404.555.0187 cell
404.555.0142 fax

```html
<!DOCTYPE html>
<html lang="en">
<head>
<meta charset="utf-8">
<title>Brightpath Care — Business Card</title>
<link rel="stylesheet" href="https://fonts.googleapis.com/css2?family=Cinzel:wght@600&family=Open+Sans:wght@400&display=swap">
<style>
  :root {
    --backdrop: #ecebef;
    --purple-light: #9077c6;
    --purple-deep: #5a3c96;
    --purple-ink: #5b3f98;
    --white: #ffffff;
    --shadow: rgba(40, 25, 70, 0.22);
  }
  * { box-sizing: border-box; margin: 0; padding: 0; }
  html, body {
    width: 1200px; height: 891px; overflow: hidden;
    background: var(--backdrop);
  }
  .canvas { position: relative; width: 1200px; height: 891px; }
  .card {
    position: absolute; left: 290px; width: 620px; height: 354px;
    border-radius: 14px; overflow: hidden;
    box-shadow: 0 14px 30px var(--shadow);
  }
  .card-back {
    top: 60px;
    background: linear-gradient(135deg, var(--purple-light) 0%, var(--purple-deep) 100%);
    display: flex; align-items: center; justify-content: center;
  }
  .card-front { top: 477px; background: var(--white); }
  .front-band { position: absolute; inset: 0; width: 100%; height: 100%; }
  .brand {
    display: flex; align-items: center; gap: 14px;
    font-family: "Cinzel", serif; font-weight: 600;
    letter-spacing: 0.02em; white-space: nowrap;
  }
  .brand-dot { border-radius: 50%; flex: none; }
  .card-back .brand { color: var(--white); font-size: 36px; }
  .card-back .brand-dot { width: 22px; height: 22px; background: var(--white); }
  .card-front .brand {
    position: absolute; left: 38px; top: 218px;
    color: var(--purple-ink); font-size: 22px; gap: 10px;
  }
  .card-front .brand-dot { width: 14px; height: 14px; background: var(--purple-ink); }
  .contact {
    position: absolute; right: 34px; top: 108px;
    text-align: right; color: var(--white);
    font-family: "Open Sans", sans-serif; white-space: nowrap;
  }
  .contact-name { font-size: 18px; }
  .contact-title { font-size: 12px; margin-top: 4px; }
  .contact-phones { margin-top: 34px; font-size: 14px; line-height: 1.75; }
</style>
</head>
<body>
<main class="canvas">
  <section class="card card-back">
    <div class="brand"><span class="brand-dot"></span>Brightpath Care</div>
  </section>

  <section class="card card-front">
    <svg class="front-band" viewBox="0 0 620 354" preserveAspectRatio="none" aria-hidden="true">
      <defs>
        <linearGradient id="bandFill" x1="0" y1="0" x2="1" y2="1">
          <stop offset="0" stop-color="#6a4ea8"/>
          <stop offset="1" stop-color="#8a70c2"/>
        </linearGradient>
      </defs>
      <path d="M300 0 C 270 110, 290 240, 410 354 L620 354 L620 0 Z" fill="url(#bandFill)"/>
    </svg>
    <div class="brand"><span class="brand-dot"></span>Brightpath Care</div>
    <div class="contact">
      <p class="contact-name">Lorraine Pettaway RN, MSN</p>
      <p class="contact-title">MHA Nurse Educator</p>
      <p class="contact-phones">404.555.0187 : M<br>404.555.0142 : F</p>
    </div>
  </section>
</main>
</body>
</html>
```